Moving Company Website

We need a webdesign for an established moving company in the Bay Area. We have chosen a wordpress template (see attached) and would like to revamp the design to give it a touch and feel of a leading moving company.
The design should be inspired by the following companies:
http://www.brisklane.com/
http://www.pkhaulers.com/
Updates

The design should be based on the following WordPress template:

http://www.layoutvault.com/demo/35782.html

And based on the image I have attached.

We will get the template PSD after we will choose a designer.

Thanks
Trevor 

Industry/Entity Type

Moving Company

Requirements
Must have
• Request a quote form must be implemented in all pages
inner pages with destinations

```html
<!DOCTYPE html>
<html lang="en">
<head>
<meta charset="utf-8">
<title>Halvern GreenShift – Moving Company</title>
<link href="https://fonts.googleapis.com/css2?family=Arimo:wght@400;700&family=Open+Sans:wght@400;600&display=swap" rel="stylesheet">
<style>
:root{
  --green:#0a9a35;
  --green-dark:#067a2a;
  --logo-green:#0c7a45;
  --ink:#222;
  --muted:#444;
  --heading:#4a4a4a;
  --panel:#262626;
  --field:#3a3a3a;
  --footer-top:#5a5a5a;
  --footer-bot:#222;
  --white:#fff;
}
*{box-sizing:border-box;margin:0;padding:0}
html,body{width:946px;height:1200px;overflow:hidden;background:#fff}
body{font-family:"Arimo",Arial,sans-serif;color:var(--ink)}
.page{position:relative;width:946px;height:1200px;overflow:hidden}
.abs{position:absolute}

/* header */
.site-header{position:absolute;left:0;top:0;width:946px;height:128px;background:linear-gradient(#fff,#ececec);border-bottom:1px solid #ddd}
.brand{position:absolute;left:74px;top:18px;color:var(--logo-green);font-family:"Arimo",sans-serif;font-weight:700;line-height:1}
.brand .line1{font-size:38px;letter-spacing:1px;display:block}
.brand .line2{font-size:38px;display:block;margin-top:10px}
.social{position:absolute;left:666px;top:12px;display:flex;align-items:center;gap:6px;font-size:10.5px;color:#333}
.social span.sq{width:18px;height:18px;border-radius:4px;display:inline-block}
.nav{position:absolute;left:375px;top:82px;display:flex;font-size:10.5px;color:#333}
.nav a{text-decoration:none;color:#333;height:24px;line-height:24px;padding:0 11.5px}
.nav a.active{background:var(--green);color:#fff;padding:0 10px}

/* hero */
.hero-photo{left:86px;top:129px;width:515px;height:336px;
  background:linear-gradient(172deg,#8f9497 0%,#b3b7b9 14%,#dfe2e3 26%,#f4f5f5 40%,#eceeef 56%,#b9bcbe 64%,#6f7274 72%,#3f4142 82%,#5a5c5d 92%,#77797a 100%)}
.estimate{left:604px;top:127px;width:252px;height:338px;background:var(--panel)}
.estimate-head{height:65px;background:linear-gradient(#505050,#2c2c2c);display:flex;align-items:center;padding-left:10px;gap:10px}
.estimate-head h2{font-family:"Open Sans",sans-serif;font-weight:400;font-size:18.5px;color:#eee;white-space:nowrap}
.field{position:absolute;left:16px;width:204px;height:27px;border:1px solid #555;border-radius:4px;background:var(--field);color:#ddd;font-size:12.5px;line-height:25px;padding-left:29px}
.submit{position:absolute;left:141px;top:300px;width:79px;height:25px;border-radius:13px;background:linear-gradient(#23c24a,#08892b);border:1px solid #9be0a8;color:#fff;font-size:12.5px;text-align:center;line-height:23px}

/* feature columns */
.feature{position:absolute;top:497px;width:184px}
.feature h3{font-family:"Open Sans",sans-serif;font-weight:600;font-size:16px;letter-spacing:1px;color:var(--heading);margin-left:3px;height:27px}
.feature .thumb{width:180px;height:128px}
.feature p{margin-top:13px;font-size:9.4px;line-height:14.8px;color:var(--muted);letter-spacing:.4px;text-align:justify}
.feature p b{color:#222}
.feature ul{list-style:none;margin-top:11px}
.feature li{font-size:9.4px;line-height:18px;color:var(--muted);letter-spacing:.4px;padding-left:15px;position:relative}
.feature li:before{content:"";position:absolute;left:4px;top:6px;border-left:4px solid #444;border-top:3px solid transparent;border-bottom:3px solid transparent}
.more{display:flex;align-items:center;gap:6px;font-size:10px;color:#111;margin:10px 0 0 4px}

.divider{left:70px;top:778px;width:799px;border-top:1px dotted #aaa}
.why{left:82px;top:792px;width:780px}
.why h2{font-family:"Open Sans",sans-serif;font-weight:600;font-size:19px;letter-spacing:1.5px;color:#111}
.why .lead{margin-top:11px;font-size:10.9px;line-height:15px;color:#111}
.why-col{position:absolute;top:872px;width:372px;font-size:9.4px;line-height:14.8px;letter-spacing:.45px;color:var(--muted);text-align:justify}
.why-col b{color:#222}

/* footer */
.footer-main{left:0;top:973px;width:946px;height:165px;background:linear-gradient(var(--footer-top),var(--footer-bot))}
.mover-art{left:64px;top:987px;width:121px;height:148px;background:linear-gradient(160deg,#d8d8d8 0%,#bdbdbd 55%,#2fb14c 56%,#1e8f3a 100%);border-radius:4px}
.foot-col{position:absolute;top:987px;width:186px;color:#eee}
.foot-col h3{font-family:"Open Sans",sans-serif;font-weight:400;font-size:17.5px;letter-spacing:1px;margin-left:2px}
.foot-col p{margin-top:10px;font-size:9.4px;line-height:14.8px;letter-spacing:.45px;text-align:justify}
.foot-col .more{color:#eee;margin-top:8px}
.testimonial{position:absolute;left:684px;top:1024px;width:181px;height:73px;background:#c9c9c9;border:1px solid #ddd;padding:5px 5px;font-size:9.4px;line-height:14.8px;letter-spacing:.4px;color:#333;text-align:justify}
.testimonial b{color:#222}
.footer-bar{left:0;top:1138px;width:946px;height:62px;background:var(--green);border-top:1px solid #3bc05c}
.footer-brand{position:absolute;left:79px;top:12px;color:#fff;font-weight:700;font-size:17px;line-height:19px}
.footer-links{position:absolute;right:80px;top:9px;display:flex;font-size:11px;color:#fff}
.footer-links span.sep{margin:0 13px}
.copyright{position:absolute;right:80px;top:35px;font-size:11px;color:#fff}
</style>
</head>
<body>
<div class="page">

  <header class="site-header">
    <div class="brand"><span class="line1">HALVERN</span><span class="line2">GreenShift</span></div>
    <div class="social">SOCIALIZE WITH US : -
      <span class="sq" style="background:#f08a1c"></span>
      <span class="sq" style="background:#5bb4e5"></span>
      <span class="sq" style="background:#3b5a9a"></span>
      <span class="sq" style="background:#26a9e0;border-radius:50%"></span>
    </div>
    <nav class="nav">
      <a class="active">HOME</a><a>ABOUT US</a><a>SERVICES</a><a>PRODUCTS</a><a>PARTNERS</a><a>NEWS</a><a>CONTACT US</a>
    </nav>
  </header>

  <div class="abs hero-photo" role="img" aria-label="Photo of a white branded moving truck speeding along a highway under a grey sky"></div>

  <section class="abs estimate">
    <div class="estimate-head">
      <svg width="34" height="34" viewBox="0 0 40 40"><circle cx="20" cy="20" r="18" fill="#fff"/><circle cx="20" cy="20" r="14" fill="#1aa83f"/><path d="M20 11v14M13 19l7 7 7-7" stroke="#fff" stroke-width="3.5" fill="none" stroke-linecap="round" stroke-linejoin="round"/></svg>
      <h2>Request an Estimate</h2>
    </div>
    <div class="field" style="top:93px">First Name</div>
    <div class="field" style="top:133px">Last Name</div>
    <div class="field" style="top:172px">Email</div>
    <div class="field" style="top:212px">Phone</div>
    <div class="field" style="top:252px">Select Service</div>
    <div class="submit">Submit</div>
  </section>

  <section class="feature" style="left:76px">
    <h3>MOVING</h3>
    <div class="thumb" role="img" aria-label="Photo of a red truck on a winding country road" style="background:linear-gradient(#8a9a5a,#6b7a45 50%,#555 100%)"></div>
    <p><b>Lorem Ipsum is simply dummy text of the printing and typesetting</b> industry. Lorem Ipsum has been the industry's standard dummy text ever since the 1500s, when an unknown printer took</p>
    <div class="more">Read more <svg width="12" height="12" viewBox="0 0 12 12"><circle cx="6" cy="6" r="5.3" fill="none" stroke="#222"/><path d="M5 3.5 7.5 6 5 8.5" fill="none" stroke="#222" stroke-width="1.3"/></svg></div>
  </section>
  <section class="feature" style="left:278px">
    <h3>STORAGE</h3>
    <div class="thumb" role="img" aria-label="Photo of a man checking boxes in a storage warehouse" style="background:linear-gradient(90deg,#c99a6a,#e8ded2 55%,#7f96b8)"></div>
    <p><b>Lorem Ipsum is simply dummy text of the printing and typesetting</b> industry. Lorem Ipsum has been the industry's standard dummy text ever since the 1500s, when an unknown printer took</p>
    <div class="more">Read more <svg width="12" height="12" viewBox="0 0 12 12"><circle cx="6" cy="6" r="5.3" fill="none" stroke="#222"/><path d="M5 3.5 7.5 6 5 8.5" fill="none" stroke="#222" stroke-width="1.3"/></svg></div>
  </section>
  <section class="feature" style="left:478px">
    <h3>SERVICES</h3>
    <div class="thumb" role="img" aria-label="Photo of two movers carrying a sofa from a truck" style="background:linear-gradient(160deg,#b89a78,#d9cbb4 50%,#6f8a4d)"></div>
    <p><b>Lorem Ipsum is simply dummy text of the printing and typesetting</b> industry. Lorem Ipsum has been the industry's standard dummy text ever since the 1500s, when an unknown printer took</p>
    <div class="more">Read more <svg width="12" height="12" viewBox="0 0 12 12"><circle cx="6" cy="6" r="5.3" fill="none" stroke="#222"/><path d="M5 3.5 7.5 6 5 8.5" fill="none" stroke="#222" stroke-width="1.3"/></svg></div>
  </section>
  <section class="feature" style="left:682px">
    <h3>VIDEOS</h3>
    <div class="thumb" role="img" aria-label="Video still of a forklift loading goods in a warehouse" style="background:linear-gradient(#c9c9c9,#9a8f88 60%,#e4e4e4 86%,#f2f2f2 87%)"></div>
    <ul>
      <li>Lorem Ipsum is simply dummy text</li>
      <li>Lorem Ipsum is simply dummy text</li>
      <li>Lorem Ipsum is simply dummy text</li>
      <li>Lorem Ipsum is simply dummy text</li>
    </ul>
    <div class="more">Read more <svg width="12" height="12" viewBox="0 0 12 12"><circle cx="6" cy="6" r="5.3" fill="none" stroke="#222"/><path d="M5 3.5 7.5 6 5 8.5" fill="none" stroke="#222" stroke-width="1.3"/></svg></div>
  </section>

  <div class="abs divider"></div>

  <section class="abs why">
    <h2>WHY US ?</h2>
    <p class="lead">Lorem Ipsum is simply dummy text of the printing and typesetting industry. Lorem Ipsum has been the industry's standard dummy text ever since the 1500s, when an unknown printer took .Lorem Ipsum is simply dummy text of the printing and typesetting industry. Lorem Ipsum has been the industry's standard</p>
  </section>
  <p class="why-col" style="left:83px"><b>Lorem Ipsum is simply dummy text of the printing and typesetting</b> industry. Lorem Ipsum has been the industry's standard dummy text ever since the 1500s, when an unknown printer took .industry. Lorem Ipsum has been the industry's standard dummy text ever since the 1500s, when an unknown printer took industry.</p>
  <p class="why-col" style="left:485px"><b>Lorem Ipsum is simply dummy text of the printing and typesetting</b> industry. Lorem Ipsum has been the industry's standard dummy text ever since the 1500s, when an unknown printer took .industry. Lorem Ipsum has been the industry's standard dummy text ever since the 1500s, when an unknown printer took industry.</p>

  <footer>
    <div class="abs footer-main"></div>
    <div class="abs mover-art" role="img" aria-label="Illustration of a mover lifting green boxes"></div>
    <section class="foot-col" style="left:218px">
      <h3>About us</h3>
      <p><b>Lorem Ipsum is simply dummy text of the printing and typesetting</b> industry. Lorem Ipsum has been the industry's standard dummy text ever since the 1500s, when an unknown printer took</p>
      <div class="more">Read more <svg width="12" height="12" viewBox="0 0 12 12"><circle cx="6" cy="6" r="5.3" fill="none" stroke="#eee"/><path d="M5 3.5 7.5 6 5 8.5" fill="none" stroke="#eee" stroke-width="1.3"/></svg></div>
    </section>
    <section class="foot-col" style="left:452px">
      <h3>Research</h3>
      <p><b>Lorem Ipsum is simply dummy text of the printing and typesetting</b> industry. Lorem Ipsum has been the industry's standard dummy text ever since the 1500s, when an unknown printer took</p>
      <div class="more">Read more <svg width="12" height="12" viewBox="0 0 12 12"><circle cx="6" cy="6" r="5.3" fill="none" stroke="#eee"/><path d="M5 3.5 7.5 6 5 8.5" fill="none" stroke="#eee" stroke-width="1.3"/></svg></div>
    </section>
    <section class="foot-col" style="left:686px">
      <h3>Testimonials</h3>
    </section>
    <div class="testimonial"><b>Lorem Ipsum is simply dummy text of the printing and typesetting</b> industry. Lorem Ipsum has been the industry's standard dummy text</div>
    <svg class="abs" style="left:696px;top:1096px" width="34" height="15" viewBox="0 0 34 15"><path d="M6 0h24C26 8 16 13 2 14 10 10 9 5 6 0z" fill="#c9c9c9"/></svg>

    <div class="abs footer-bar">
      <div class="footer-brand">HALVERN<br>GreenShift</div>
      <div class="footer-links">Home<span class="sep">|</span>About Us<span class="sep">|</span>Services<span class="sep">|</span>Products<span class="sep">|</span>Partners<span class="sep">|</span>News<span class="sep">|</span>Contact us</div>
      <div class="copyright">©2012 Northgate Relocation Co. US DOT 402915 | MC 175520</div>
    </div>
  </footer>

</div>
</body>
</html>
```